Kindling Haven of Alabama

We are a disaster relief nonprofit organization that provides relief to families children and pets when a disaster strikes multifamily. We need a easy and powerful piece that tells what we do and draws folks into finding out more. So a piece that could be used at tradeshows or speaking engagements
Updates

Be sure to include our social and other contact info. Added Monday, October 16, 2017

Target Market(s)

Potential Donors & Volunteers

Industry/Entity Type

Non-Profit

Font styles to use
Serif

Colors

Designer to choose colors to be used in the design.

Requirements
Must have
• Our logo and trigger photos I am going to rely on your expertise to create something compelling that is simple and powerful
Nice to have
• Moving pull on the heart strings

```html
<!DOCTYPE html>
<html lang="en">
<head>
<meta charset="utf-8">
<title>Kindling Haven of Alabama – Disaster Relief</title>
<link rel="stylesheet" href="https://fonts.googleapis.com/css2?family=Cormorant+SC:wght@700&family=Gelasio:wght@400;700&display=swap">
<style>
  :root {
    --paper: #ffffff;
    --frame: #b9b9b9;
    --navy: #1f2a6b;
    --ink: #36368a;
    --brand: #2a3b9a;
    --sky: #2f8fd8;
    --gold: #d8b24c;
    --orange: #f08a2c;
  }
  * { box-sizing: border-box; margin: 0; padding: 0; }
  html, body { width: 1200px; height: 858px; overflow: hidden; background: var(--paper); }
  .flyer {
    position: relative;
    width: 1200px;
    height: 858px;
    border: 2px solid var(--frame);
    background: var(--paper);
    font-family: "Gelasio", Georgia, serif;
  }
  .brand { position: absolute; left: 48px; top: 44px; width: 520px; color: var(--brand); font-family: "Gelasio", Georgia, serif; font-weight: 400; }
  .brand__line { display: block; line-height: 1; }
  .brand__line--lead { font-size: 104px; }
  .brand__line--main { font-size: 104px; margin-top: 12px; }
  .brand__line--place { font-size: 50px; margin-top: 26px; }
  .brand__dot { position: absolute; left: 440px; top: 2px; width: 34px; height: 34px; border-radius: 50%; background: var(--sky); }

  .photo { position: absolute; border: 2px solid var(--gold); }
  .photo--rescue { left: 614px; top: 50px; width: 548px; height: 310px; background: linear-gradient(180deg, #c9ccd2 0%, #8e9a8a 38%, #6f6a5c 62%, #a89c86 100%); }
  .photo--fire { left: 38px; top: 408px; width: 254px; height: 338px; background: linear-gradient(160deg, #6e8fb4 0%, #e06a1e 35%, #f4a23a 55%, #3b2a1c 100%); }
  .photo--kits { left: 319px; top: 516px; width: 416px; height: 230px; border: none; background: linear-gradient(120deg, #2c2c30 0%, #b89a74 40%, #e9e4dc 70%, #d4c3a8 100%); }

  .headline {
    position: absolute; left: 318px; top: 400px; width: 430px;
    font-family: "Cormorant SC", "Times New Roman", serif; font-weight: 700;
    font-size: 24px; line-height: 31px; color: var(--navy); letter-spacing: 0.3px;
  }
  .accent-bar { position: absolute; left: 764px; top: 384px; width: 18px; height: 362px; background: var(--orange); }
  .story {
    position: absolute; left: 814px; top: 382px; width: 360px;
    font-weight: 700; font-size: 20.5px; line-height: 32.5px; color: var(--ink);
  }
  .rule { position: absolute; left: 22px; right: 16px; top: 772px; height: 2px; background: var(--orange); }
  .callout {
    position: absolute; left: 0; top: 790px; width: 100%; height: 50px;
    font-family: "Cormorant SC", "Times New Roman", serif; font-weight: 700;
    font-size: 31px; color: var(--navy);
  }
  .callout__mark { position: absolute; top: 12px; width: 26px; height: 26px; border-radius: 50%; background: var(--sky); }
  .callout__need { position: absolute; left: 128px; top: 4px; }
  .callout__help { position: absolute; left: 832px; top: 4px; }
  .callout__help u { font-style: italic; }
</style>
</head>
<body>
<main class="flyer">
  <div class="brand" aria-label="Kindling Haven of Alabama">
    <span class="brand__dot"></span>
    <span class="brand__line brand__line--lead">Kindling</span>
    <span class="brand__line brand__line--main">Haven</span>
    <span class="brand__line brand__line--place">of Alabama</span>
  </div>

  <div class="photo photo--rescue" role="img" aria-label="Rescuers wading through floodwater guiding a boat carrying a family"></div>
  <div class="photo photo--fire" role="img" aria-label="A multifamily home engulfed in flames behind a pine tree"></div>

  <h2 class="headline">Life-Saving Disaster Relief<br>for Displaced Residents Across<br>The Great State of Alabama</h2>

  <div class="photo photo--kits" role="img" aria-label="A smiling boy holding a relief kit box and a teddy bear at the back of a loaded car"></div>

  <div class="accent-bar"></div>
  <p class="story">There are few things in life that feel more hopeless than watching your home go up in flames. Kindling Haven provides kits which include essentials crucial for the survival of displaced families. Kits also contain notes of hope and encouragement by Alabama students, AND cuddly Haven Bears !!!</p>

  <div class="rule"></div>
  <div class="callout">
    <span class="callout__mark" style="left:60px"></span>
    <span class="callout__need">Citizens of Alabama Are In Need !</span>
    <span class="callout__mark" style="left:766px"></span>
    <span class="callout__help"><u>You</u> Can Help!</span>
    <span class="callout__mark" style="left:1126px"></span>
  </div>
</main>
</body>
</html>
```